Website Homepage Design

Daltrove Care Partners Inc. is a Canadian financial services company that specialize in the delivery and administration of alternative health benefit solutions. Daltrove is seeking to adjust their brand and develop a new website.

We like the design and layout of the website below but are not looking for an exact replica (be creative):

http://www.quellaretreat.example/

We want the colour scheme to be clean white and "fresh green", possibly with orange accents (links).

This posting is only for a website homepage design (no coding), but anyone who includes a new logo, in addition to the design, will get priority.

Best of luck,

Oliver
Updates

Project is guaranteed.

Please let me know if you are currently working on a design.

Thank you,

Oliver

*Update:

Two example websites with good colour scheme/design:

- http://budlynest.example/
- http://www.petalkinderhaus.example.au/

I have attached a wireframe and colour scheme to the project brief. The main colour should be the green one. Other colours can be used for highlights and accents, etc.

Target Market(s)

Business owners age 50+

Industry/Entity Type

Financial

Requirements
Must have
• - Clear and simple design
- Area for video (similar to http://www.quellaretreat.example)
Should not have
• - Lots of pictures

```html
<!DOCTYPE html>
<html lang="en">
<head>
<meta charset="utf-8">
<title>Daltrove Care Partners Inc. — Home</title>
<link href="https://fonts.googleapis.com/css2?family=Arimo:wght@400;700&family=Roboto+Condensed:wght@700&family=PT+Serif&display=swap" rel="stylesheet">
<style>
:root{
  --green-top:#b9d152;
  --green-bottom:#9fbb30;
  --green-dark:#77981f;
  --green-link:#8aab1e;
  --orange:#f39a12;
  --text:#444;
  --heading:#222;
  --white:#fff;
  --border:#e4e4e4;
  --news-bg:#f1f5dc;
}
*{box-sizing:border-box;margin:0;padding:0}
html,body{width:1200px;height:942px;overflow:hidden}
body{position:relative;font-family:Arimo,Arial,sans-serif;color:var(--text);
  background:linear-gradient(#dcdcdc 106px,#f2f2f2 260px,#ffffff 520px,#ffffff)}
a{text-decoration:none;color:inherit}
.site-header{position:absolute;left:0;top:0;width:1200px;height:106px;
  background:linear-gradient(var(--green-top),var(--green-bottom));border-bottom:1px solid #93ad2a}
.brand{position:absolute;left:200px;top:40px;display:flex;align-items:center;gap:8px;
  color:var(--white);font-family:"Roboto Condensed",sans-serif;font-weight:700;font-size:22px;letter-spacing:1px}
.brand-dot{width:14px;height:14px;border-radius:50%;background:var(--white)}
.account-links{position:absolute;left:959px;top:12px;font-size:12px;font-weight:700;color:#3a4a10}
.account-links span{margin:0 8px}
.main-nav{position:absolute;left:372px;top:69px;display:flex;height:37px}
.main-nav a{font-family:"Roboto Condensed",sans-serif;font-weight:700;font-size:13px;color:var(--white);
  line-height:37px;padding:0 17px;letter-spacing:.3px}
.main-nav a.active{background:var(--green-dark);padding:0 20px}
.search{position:absolute;left:909px;top:74px;width:158px;height:24px;background:var(--white);
  border:1px solid #8ca52a;border-radius:3px}
.search svg{position:absolute;right:6px;top:4px}
.content-panel{position:absolute;left:189px;top:135px;width:872px;height:530px;background:var(--white);
  box-shadow:0 0 6px rgba(0,0,0,.08)}
.hero{position:absolute;left:208px;top:153px;width:835px;height:305px;
  background:linear-gradient(#f7a83a,#fbd079 45%,#fad38c 62%,#e98a2a 82%,#c9531d)}
.hero-title{position:absolute;left:208px;top:266px;width:835px;text-align:center;
  font-size:31px;color:#6a5636;letter-spacing:-.3px}
.hero-arrow{position:absolute;top:283px;width:35px;height:37px;background:var(--white);
  display:flex;align-items:center;justify-content:center}
.hero-arrow.prev{left:208px;border-radius:0 4px 4px 0}
.hero-arrow.next{left:1007px;border-radius:4px 0 0 4px}
.hero-controls{position:absolute;left:588px;top:417px;width:78px;height:33px;background:rgba(255,255,255,.45);
  display:flex;align-items:center;justify-content:center;gap:8px}
.hero-cta{position:absolute;left:893px;top:423px;width:138px;height:28px;border-radius:14px;
  background:linear-gradient(#b8d24a,#8eaf20);color:var(--white);font-size:13px;line-height:28px;padding-left:18px}
.hero-cta svg{position:absolute;right:8px;top:7px}
.plan-card{position:absolute;top:476px;width:265px;height:149px;border:2px solid #eee;background:var(--white);padding:10px 8px 10px 18px}
.plan-card h2{font-family:"PT Serif",Georgia,serif;font-weight:400;font-size:24px;line-height:28px;color:var(--heading)}
.plan-card h3{font-size:11.5px;line-height:15px;font-weight:700;color:var(--orange);margin-top:2px}
.plan-card p{font-size:11px;line-height:16.6px;margin-top:1px}
.read-more{position:absolute;font-size:11px;font-weight:700;border-bottom:1px solid currentColor}
.plan-card .read-more{right:22px;bottom:6px;color:var(--green-link)}
.section-title{position:absolute;font-family:"Roboto Condensed",sans-serif;font-weight:700;font-size:17px;color:var(--heading)}
.about{position:absolute;left:213px;top:701px;width:542px;height:160px;background:#f8f8f8;border:1px solid var(--border);border-top:4px solid #e4e4e4;overflow:hidden}
.about h3{position:absolute;left:23px;top:14px;font-size:15px;color:#333}
.about h3 em{font-style:normal;font-weight:400;color:var(--orange)}
.about p{position:absolute;left:22px;top:44px;width:360px;font-size:11px;line-height:16.6px}
.about .read-more{left:298px;top:140px;color:#333}
.about-photo{position:absolute;left:384px;top:32px;width:158px;height:124px;
  background:linear-gradient(135deg,#f4d9c2,#d9e6f2 60%,#b9d4e8)}
.news{position:absolute;left:782px;top:701px;width:256px;height:161px;background:var(--news-bg);
  border:1px solid #e0e6c4;border-top:3px solid var(--green-bottom);padding:18px 20px}
.news time{font-size:10.5px;font-weight:700;color:#6d7a2a}
.news p{font-size:11px;line-height:16.6px;margin-top:8px}
.news .read-more{left:22px;top:140px;color:#333}
.site-footer{position:absolute;left:0;top:906px;width:1200px;height:36px;background:var(--green-bottom);
  border-top:2px solid #c8da7a;color:#f4f8e2;font-size:11.5px}
.site-footer .copy{position:absolute;left:220px;top:10px}
.site-footer nav{position:absolute;right:169px;top:11px}
</style>
</head>
<body>
<header class="site-header">
  <a class="brand" href="#"><span class="brand-dot"></span>DALTROVE</a>
  <div class="account-links"><a href="#">Login</a><span>I</span><a href="#">Register</a></div>
  <nav class="main-nav">
    <a class="active" href="#">HOME</a><a href="#">ABOUT US</a><a href="#">FORMS</a><a href="#">CUSTOMER CARE</a><a href="#">FAQ</a><a href="#">CONTACT US</a>
  </nav>
  <div class="search"><svg width="14" height="14" viewBox="0 0 14 14"><circle cx="5.5" cy="5.5" r="4" fill="none" stroke="#444" stroke-width="2"/><line x1="8.5" y1="8.5" x2="13" y2="13" stroke="#444" stroke-width="2.4"/></svg></div>
</header>

<div class="content-panel"></div>
<div class="hero" role="img" aria-label="Autumn leaves along the bottom of a warm orange sky"></div>
<p class="hero-title">The group way isn’t always the best way.</p>
<a class="hero-arrow prev" href="#"><svg width="14" height="18" viewBox="0 0 14 18"><path d="M11 2 4 9l7 7" fill="none" stroke="#444" stroke-width="3.5"/></svg></a>
<a class="hero-arrow next" href="#"><svg width="14" height="18" viewBox="0 0 14 18"><path d="M3 2l7 7-7 7" fill="none" stroke="#444" stroke-width="3.5"/></svg></a>
<div class="hero-controls">
  <svg width="22" height="22" viewBox="0 0 22 22"><circle cx="11" cy="11" r="10" fill="#333"/><rect x="7" y="6" width="3" height="10" fill="#fff"/><rect x="12" y="6" width="3" height="10" fill="#fff"/></svg>
  <svg width="22" height="22" viewBox="0 0 22 22"><circle cx="11" cy="11" r="10" fill="#333"/><path d="M6 9h3l4-3v10l-4-3H6z" fill="#fff"/></svg>
</div>
<a class="hero-cta" href="#">Find out more...<svg width="14" height="14" viewBox="0 0 14 14"><circle cx="7" cy="7" r="7" fill="#6f8f14"/><path d="M5.5 4l4 3-4 3z" fill="#fff"/></svg></a>

<article class="plan-card" style="left:206px">
  <h2>Smallbiz</h2>
  <h3>Cut your healthcare costs in half</h3>
  <p>If you’re a sole proprietor, professional or small business owner, you have three ways to fund your health and dental costs.</p>
  <a class="read-more" href="#">Read More...</a>
</article>
<article class="plan-card" style="left:490px">
  <h2>Bigbiz</h2>
  <h3>Save 20% to 30% on benefit plan costs</h3>
  <p>If you have a small or medium-sized business, chances are you’ve been hit hard by increasing premiums.</p>
  <a class="read-more" href="#">Read More...</a>
</article>
<article class="plan-card" style="left:775px">
  <h2>Brokerbiz</h2>
  <h3>Win more business</h3>
  <p>As a broker / agent, you’re looking for ways to attract new clients, and ways to retain those clients who are becoming increasingly frustrated with traditional plans.</p>
  <a class="read-more" href="#">Read More...</a>
</article>

<h2 class="section-title" style="left:238px;top:670px">About Daltrove</h2>
<section class="about">
  <h3>We make it <em>easy</em>. we make it <em>affordable</em>.</h3>
  <p>We’re a Canadian financial services company with our head office in Vancouver. We specialize in the delivery and administration of alternative health benefit solutions. We respond to the needs of companies with one to 2500 employees who are looking to control their health benefit costs by offering options that are flexible and that respect the bottom line.</p>
  <div class="about-photo" role="img" aria-label="Photo of a smiling family of four"></div>
  <a class="read-more" href="#">Read More...</a>
</section>

<h2 class="section-title" style="left:801px;top:671px">Latest News &amp; Events</h2>
<section class="news">
  <time>May 12, 2011</time>
  <p><b>Lorem Ipsum is simply</b> dummy text of the printing and typesetting industry. Lorem Ipsum has been the industry’s standard dummy text ever since the 1500s</p>
  <a class="read-more" href="#">Read More...</a>
</section>

<footer class="site-footer">
  <div class="copy">© 2011 daltrove.example &nbsp;I &nbsp;&nbsp;Care Partners Inc.</div>
  <nav><a href="#">Home</a> I <a href="#">About us</a> I <a href="#">News</a> I &nbsp;<a href="#">FAQ</a> I <a href="#">Contact</a></nav>
</footer>
</body>
</html>
```